business card design and letterhead for a building inspection company. We have a pre-purchase building and pest inspection ( i inspect house before people purchase it)
Updates

Tilda has been so so responsive and good, i highly recommend her

Industry/Entity Type

Building

Contact Information for Business Card

audience, solicitor, real estate agent, mortgage brokerthe rest of the info will be in the attachement business card

```html
<!DOCTYPE html>
<html lang="en">
<head>
<meta charset="utf-8">
<title>Truehome Property Inspections – Business Card</title>
<link rel="stylesheet" href="https://fonts.googleapis.com/css2?family=Lato:wght@400;700;900&family=Montserrat:wght@600&display=swap">
<style>
  :root {
    --backdrop: #3a322e;
    --card: #ffffff;
    --brand-blue: #1f7fcf;
    --ink: #151515;
    --rule-blue: #1f6fb5;
  }
  * { box-sizing: border-box; margin: 0; padding: 0; }
  html, body { width: 1200px; height: 589px; overflow: hidden; }
  body {
    background: var(--backdrop);
    font-family: "Lato", Arial, sans-serif;
    position: relative;
  }
  .card {
    position: absolute;
    top: 146px;
    width: 520px;
    height: 297px;
    background: var(--card);
    border-radius: 18px;
    overflow: hidden;
    box-shadow: 0 14px 30px rgba(0,0,0,.45);
  }
  .card--front { left: 50px; }
  .card--back { left: 630px; }
  .card-band { position: absolute; left: 0; top: 0; width: 520px; height: 297px; }

  .brand {
    position: absolute;
    display: flex;
    align-items: center;
    gap: 10px;
  }
  .brand-square {
    width: 26px; height: 26px;
    border: 4px solid var(--brand-blue);
    border-radius: 3px;
  }
  .brand-name {
    color: var(--brand-blue);
    font-weight: 900;
    font-size: 24px;
    line-height: 1.05;
    letter-spacing: .5px;
    text-transform: uppercase;
  }
  .card--front .brand { left: 92px; top: 62px; }
  .card--back .brand { left: 178px; top: 42px; }

  .tagline {
    position: absolute;
    left: 0; width: 100%;
    top: 160px;
    text-align: center;
    font-family: "Montserrat", Arial, sans-serif;
    font-weight: 600;
    font-size: 12px;
    letter-spacing: 4px;
    color: var(--ink);
  }

  .holder { position: absolute; left: 40px; top: 118px; }
  .holder-name { color: var(--brand-blue); font-weight: 900; font-size: 20px; }
  .holder-role { color: var(--ink); font-weight: 900; font-size: 11px; letter-spacing: .5px; margin-top: 2px; }

  .divider {
    position: absolute; left: 262px; top: 118px;
    width: 2px; height: 62px; background: var(--rule-blue);
  }
  .contacts { position: absolute; left: 290px; top: 120px; list-style: none; }
  .contacts li {
    display: flex; align-items: center; gap: 10px;
    color: var(--rule-blue); font-weight: 700; font-size: 13px;
    height: 21px;
  }
  .contacts svg { width: 13px; height: 13px; flex: none; }

  .website {
    position: absolute; right: 26px; bottom: 44px;
    color: var(--rule-blue); font-weight: 700; font-size: 13px;
  }
</style>
</head>
<body>

<section class="card card--front" aria-label="Business card front">
  <svg class="card-band" viewBox="0 0 520 297" aria-hidden="true">
    <path d="M0 262 L250 262 Q265 262 280 252 L520 222 L520 297 L0 297 Z" fill="var(--brand-blue)"/>
    <g fill="var(--ink)">
      <path d="M262 248 L330 240 L330 246 L262 254 Z"/>
      <path d="M336 239 L402 231 L402 237 L336 245 Z"/>
      <path d="M408 230 L474 222 L474 228 L408 236 Z"/>
      <path d="M480 221 L520 216 L520 222 L480 227 Z"/>
    </g>
  </svg>
  <div class="brand">
    <span class="brand-square"></span>
    <span class="brand-name">Truehome<br>Property Inspections</span>
  </div>
  <p class="tagline">SAFE HOME... SAFE FAMILY</p>
</section>

<section class="card card--back" aria-label="Business card back">
  <svg class="card-band" viewBox="0 0 520 297" aria-hidden="true">
    <path d="M520 278 L270 278 Q255 278 240 268 L0 208 L0 297 L520 297 Z" fill="var(--brand-blue)"/>
    <g fill="var(--ink)">
      <path d="M0 188 L58 202 L58 208 L0 194 Z"/>
      <path d="M64 203 L130 219 L130 225 L64 209 Z"/>
      <path d="M136 221 L200 237 L200 243 L136 227 Z"/>
      <path d="M206 239 L262 252 L262 258 L206 245 Z"/>
    </g>
  </svg>
  <div class="brand">
    <span class="brand-square"></span>
    <span class="brand-name">Truehome<br>Property Inspections</span>
  </div>

  <div class="holder">
    <p class="holder-name">Daniel Marsh</p>
    <p class="holder-role">DIRECTOR</p>
  </div>

  <span class="divider"></span>

  <ul class="contacts">
    <li>
      <svg viewBox="0 0 16 16" aria-hidden="true"><path d="M2 5 Q8 1 14 5 L12 7 L10 6 L10 5 Q8 4 6 5 L6 6 L4 7 Z M4 8 L12 8 L13 14 L3 14 Z" fill="var(--ink)"/></svg>
      (02) 5550 1827
    </li>
    <li>
      <svg viewBox="0 0 16 16" aria-hidden="true"><rect x="4" y="1" width="8" height="14" rx="1.5" fill="none" stroke="var(--ink)" stroke-width="1.6"/></svg>
      0400 555 912
    </li>
    <li>
      <svg viewBox="0 0 16 16" aria-hidden="true"><rect x="1" y="3" width="14" height="10" fill="var(--ink)"/><path d="M1 3 L8 9 L15 3" fill="none" stroke="#fff" stroke-width="1.2"/></svg>
      info@truehomeinspections.com.au
    </li>
  </ul>

  <p class="website">www.truehomeinspections.com.au</p>
</section>

</body>
</html>
```